Front page on www.brightlanegoods.com modern service ads - each ad for each featured service

We need to have initial 5 banners to be created for our soon to be launched new site,. These are 5 rotating banners that will showcase our companies key features. We are looking for a modern stylish yet simple look to highlight these features. Something thats very inviting and modern to fit the look of the new website.

5 banners need to be, information can be found on www.brightlanegoods.com about these. Please ask if any questions

Why us?
Art Services
Order Process
Current promotions
Clearance products

please also note. the design will be going onto this website. http://new.brightlanegoods.com/ Please base actual designs , color schemes etc.. for the new site.

Target Market(s)

Small businesses that purchase marketing promotional goods, to promote their business

Industry/Entity Type

Promotional Product

Font styles to use
Sans Serif

Requirements
Must have
• Size of the banner is 965 x 400 px
Nice to have
• Modern elements,, very clean and minimal look
Should not have
• no cheap generic clip art

```html
<!DOCTYPE html>
<html lang="en">
<head>
<meta charset="utf-8">
<title>Bright Lane Goods — Feature Banners</title>
<link href="https://fonts.googleapis.com/css2?family=Montserrat:wght@400;600;700&family=Roboto:wght@500;700&display=swap" rel="stylesheet">
<style>
  :root {
    --brand-blue: #2b57a5;
    --accent-green: #5aaa2f;
    --promo-green: #6dbb3a;
    --white: #ffffff;
    --navy: #0a2159;
    --gap: #ffffff;
  }
  html, body {
    margin: 0; padding: 0;
    width: 805px; height: 1200px;
    overflow: hidden;
    background: var(--gap);
  }
  .banner-stack {
    position: absolute; left: 0; top: 0;
    width: 1400px; height: 2086px;
    transform: scale(0.575);
    transform-origin: 0 0;
    font-family: "Montserrat", sans-serif;
  }
  .banner {
    position: absolute; left: 0; width: 1400px; height: 400px;
    overflow: hidden;
  }
  .banner__photo { position: absolute; inset: 0; }
  .bracket {
    position: absolute; width: 51px;
    border: 3px solid var(--accent-green);
  }
  .bracket--left { border-right: none; }
  .bracket--right { border-left: none; }
  .bracket--top { border-bottom: none; }
  .bracket--bottom { border-top: none; }
  .title {
    position: absolute; margin: 0;
    font-weight: 700; font-size: 60px; line-height: 1;
    letter-spacing: -2px; white-space: nowrap;
  }
  .title__light { font-weight: 400; }
  .learn-more {
    position: absolute; display: flex; align-items: center; gap: 6px;
    font-weight: 600; font-size: 16px; letter-spacing: -0.5px;
    text-transform: uppercase; white-space: nowrap;
  }
  .learn-more svg { display: block; }
  .on-light { color: var(--brand-blue); }
  .on-dark { color: var(--white); }

  /* Why us */
  .banner--why { top: 0; }
  .banner--why .banner__photo {
    background:
      radial-gradient(ellipse 260px 260px at 850px 180px, #e7d3c6 0%, #d9c7bd 40%, rgba(205,205,210,0) 75%),
      radial-gradient(ellipse 200px 120px at 830px 230px, #bcd7ea 0%, rgba(188,215,234,0) 80%),
      linear-gradient(90deg, #d9d6d3 0%, #cfccca 45%, #b8b6b8 100%);
  }
  /* Art services */
  .banner--art { top: 422px; }
  .banner--art .banner__photo {
    background:
      radial-gradient(ellipse 190px 120px at 780px 610px, #b26ad6 0%, #7d3fb3 45%, rgba(60,30,120,0) 100%),
      radial-gradient(ellipse 420px 220px at 930px 480px, rgba(120,80,210,0.45) 0%, rgba(10,33,89,0) 80%),
      radial-gradient(ellipse 70px 130px at 1115px 720px, #8fd0f0 0%, #3f9ed6 55%, rgba(10,33,89,0) 100%),
      var(--navy);
  }
  /* Order process */
  .banner--order { top: 843px; }
  .banner--order .banner__photo {
    background:
      radial-gradient(ellipse 200px 210px at 430px 1080px, #e8c7ad 0%, #d9b397 45%, rgba(220,220,220,0) 90%),
      radial-gradient(ellipse 50px 90px at 290px 1075px, #9b1a22 0%, rgba(155,26,34,0) 100%),
      radial-gradient(ellipse 500px 220px at 950px 1050px, #f4f4f4 0%, rgba(244,244,244,0) 100%),
      linear-gradient(90deg, #d7d7d7 0%, #dedede 50%, #e4e4e4 100%);
  }
  /* Current promotions */
  .banner--promo { top: 1264px; }
  .banner--promo .banner__photo {
    background:
      radial-gradient(ellipse 150px 170px at 915px 1380px, #c48e76 0%, #9c6b58 50%, rgba(30,25,25,0) 100%),
      radial-gradient(ellipse 40px 40px at 290px 1365px, #e6c23c 0%, rgba(230,194,60,0) 100%),
      linear-gradient(90deg, #9b7550 0%, #6f5236 14%, #2a2320 22%, #15151a 50%, #2c3138 78%, #5d6878 100%);
  }
  /* Clearance products */
  .banner--clear { top: 1686px; }
  .banner--clear .banner__photo {
    background:
      radial-gradient(ellipse 310px 230px at 700px 1880px, #7f97dc 0%, #6d86cf 55%, rgba(86,110,190,0) 100%),
      linear-gradient(180deg, #4f6bbc 0%, #5a76c4 60%, #4a65b4 100%);
  }
  .banner__photo--offset { top: 0; }

  .price-row {
    position: absolute; top: 1499px; left: 480px;
    display: flex; font-family: "Roboto", sans-serif;
    color: var(--promo-green); font-weight: 500;
  }
  .price {
    font-size: 27px; padding: 0 20px; line-height: 34px;
    border-left: 1px solid rgba(255,255,255,0.25);
  }
  .price:first-child { border-left: none; padding-left: 16px; }
  .price__off { font-size: 15px; font-weight: 700; }
</style>
</head>
<body>
<div class="banner-stack">

  <!-- Why us -->
  <section class="banner banner--why" aria-label="Why us">
    <div class="banner__photo" role="img" aria-label="Healthcare worker wearing a face shield and surgical mask against a soft grey background"></div>
  </section>
  <div class="bracket bracket--left" style="left:218px;top:139px;height:117px;"></div>
  <div class="bracket bracket--right" style="left:571px;top:139px;height:117px;"></div>
  <h2 class="title on-light" style="left:291px;top:172px;">WHY <span class="title__light">US?</span></h2>
  <a class="learn-more on-light" style="left:340px;top:249px;">
    <svg width="40" height="8" viewBox="0 0 40 8"><line x1="0" y1="4" x2="34" y2="4" stroke="currentColor" stroke-width="1.5"/><path d="M33 0 L40 4 L33 8 Z" fill="currentColor"/></svg>Learn more</a>

  <!-- Art services -->
  <section class="banner banner--art" aria-label="Art services">
    <div class="banner__photo" style="top:-422px;height:822px;" role="img" aria-label="Glowing purple jellyfish on deep navy with a pump bottle of hand sanitizer at right"></div>
  </section>
  <div class="bracket bracket--left" style="left:430px;top:561px;height:117px;"></div>
  <div class="bracket bracket--right" style="left:916px;top:561px;height:117px;"></div>
  <h2 class="title on-dark" style="left:496px;top:595px;">ART SERVICES</h2>
  <a class="learn-more on-dark" style="left:626px;top:721px;">
    <svg width="40" height="8" viewBox="0 0 40 8"><line x1="0" y1="4" x2="34" y2="4" stroke="currentColor" stroke-width="1.5"/><path d="M33 0 L40 4 L33 8 Z" fill="currentColor"/></svg>Learn more</a>

  <!-- Order process -->
  <section class="banner banner--order" aria-label="Order process">
    <div class="banner__photo" style="top:-843px;height:1243px;" role="img" aria-label="Smiling woman holding a red branded tumbler beside soft white flowing shapes"></div>
  </section>
  <div class="bracket bracket--left" style="left:338px;top:982px;height:117px;"></div>
  <div class="bracket bracket--right" style="left:1008px;top:982px;height:117px;"></div>
  <h2 class="title on-light" style="left:452px;top:1017px;">ORDER PROCESS</h2>
  <a class="learn-more on-light" style="left:652px;top:1132px;">
    <svg width="14" height="8" viewBox="0 0 14 8"><line x1="0" y1="4" x2="8" y2="4" stroke="currentColor" stroke-width="1.5"/><path d="M7 0 L14 4 L7 8 Z" fill="currentColor"/></svg>Learn more</a>

  <!-- Current promotions -->
  <section class="banner banner--promo" aria-label="Current promotions">
    <div class="banner__photo" style="top:-1264px;height:1665px;" role="img" aria-label="Smiling man in a black t-shirt in a blurred warm interior"></div>
  </section>
  <div class="bracket bracket--left" style="left:298px;top:1418px;height:117px;"></div>
  <div class="bracket bracket--right" style="left:1048px;top:1418px;height:117px;"></div>
  <h2 class="title on-dark" style="left:351px;top:1432px;">CURRENT PROMOTIONS</h2>
  <div class="price-row">
    <span class="price">$10<span class="price__off">off</span></span>
    <span class="price">$25<span class="price__off">off</span></span>
    <span class="price">$50<span class="price__off">off</span></span>
    <span class="price">$100<span class="price__off">off</span></span>
  </div>
  <a class="learn-more on-dark" style="left:626px;top:1578px;">
    <svg width="40" height="8" viewBox="0 0 40 8"><line x1="0" y1="4" x2="34" y2="4" stroke="currentColor" stroke-width="1.5"/><path d="M33 0 L40 4 L33 8 Z" fill="currentColor"/></svg>Learn more</a>

  <!-- Clearance products -->
  <section class="banner banner--clear" aria-label="Clearance products">
    <div class="banner__photo" style="top:-1686px;height:2086px;" role="img" aria-label="Close-up of a blue respirator mask with orange straps on a blue background"></div>
  </section>
  <div class="bracket bracket--left bracket--top" style="left:458px;top:1787px;height:52px;"></div>
  <div class="bracket bracket--left bracket--bottom" style="left:458px;top:1904px;height:62px;"></div>
  <div class="bracket bracket--right bracket--top" style="left:888px;top:1787px;height:52px;"></div>
  <div class="bracket bracket--right bracket--bottom" style="left:888px;top:1904px;height:62px;"></div>
  <h2 class="title on-dark" style="left:520px;top:1815px;">CLEARANCE</h2>
  <h2 class="title on-dark" style="left:520px;top:1887px;letter-spacing:1px;">PRODUCTS</h2>
  <a class="learn-more on-dark" style="left:618px;top:2003px;">
    <svg width="40" height="8" viewBox="0 0 40 8"><line x1="0" y1="4" x2="34" y2="4" stroke="currentColor" stroke-width="1.5"/><path d="M33 0 L40 4 L33 8 Z" fill="currentColor"/></svg>Learn more</a>

</div>
</body>
</html>
```